We need a simple but upscale web site designed in word press.
A new breed boutique Investment Bank. Specializing in select cutting-edge emerging growth company financings with a focus on impact investing.
This is a customer facing site that must instill confidence,be clean, streamline and easy to navigate.

Target Market(s)

Entrepreneurs, Finance professionals, Investors

Industry/Entity Type

Bank

Number of Pages Required

5+ page

Font styles to use
Other font styles liked:
• see attached

Requirements
Must have
• Landing page
• About us
• Investors
• Entrepreneurs
• CrowdFunding
• Contact
Nice to have
• Sign up
• Similar look and feel to this site - https://tarnwickcapital.example

```html
<!DOCTYPE html>
<html lang="en">
<head>
<meta charset="utf-8">
<title>Brightfold Capital</title>
<link rel="stylesheet" href="https://fonts.googleapis.com/css2?family=Open+Sans:wght@300;400;600;700&family=Roboto+Condensed:wght@400;700&display=swap">
<style>
:root{
  --blue:#1f6fb8;
  --blue-dark:#17589a;
  --ink:#333a40;
  --muted:#7a8087;
  --grey-band:#dfe0e4;
  --card-grey:#d9dadd;
  --footer:#22262c;
  --white:#ffffff;
  --line:#c9ccd1;
}
*{box-sizing:border-box;margin:0;padding:0}
html,body{width:1200px;height:4986px;overflow:hidden}
body{position:relative;background:var(--white);font-family:"Open Sans",sans-serif;color:var(--ink)}
.abs{position:absolute}
.center{text-align:center;left:0;width:1200px}

/* hero */
.hero{top:0;left:0;width:1200px;height:864px;background:linear-gradient(120deg,#c9b39a 0%,#e7ecf1 35%,#b8cde0 65%,#eef2f6 100%)}
.nav{top:0;left:0;width:1200px;height:60px;background:linear-gradient(#4f93cf,#2d78bb);border-bottom:2px solid #1b5f9d}
.social-top{top:12px;width:36px;height:36px;border-radius:50%;background:var(--white);color:var(--blue);font-size:10px;font-weight:700;display:flex;align-items:center;justify-content:center}
.nav-link{top:16px;color:var(--white);font-size:14px}
.nav-link.active{top:10px;border:1px solid var(--white);padding:6px 10px}
.search{top:10px;left:971px;width:153px;height:40px;border:1px solid var(--white);color:var(--white);font-size:14px;padding:10px 12px}
.arrow{top:420px;font-size:40px;color:#222;font-weight:300}
.dots{top:803px;left:560px;display:flex;gap:10px}
.dot{width:16px;height:16px;border-radius:50%;background:#222}
.dot.on{background:var(--white);border:3px solid #222}

/* welcome */
.welcome{top:950px;font-size:92px;font-weight:300;color:var(--blue);letter-spacing:3px}
.brand-mark{top:1095px;left:530px;width:140px;height:140px;border-radius:50%;border:3px solid #3a3f45}
.brand-name{top:1240px;font-size:30px;font-weight:600;color:var(--blue-dark);letter-spacing:2px}
.tagline{top:1328px;font-size:24px;font-weight:400;letter-spacing:1px}
.tagline-sub{top:1365px;font-size:16px;color:#555}
.btn{background:var(--blue);color:var(--white);font-size:15px;font-weight:600;text-align:center;line-height:36px;height:36px}

/* about */
.about{top:1539px;left:0;width:1200px;height:455px;background:var(--grey-band)}
.about-ring{top:1610px;left:75px;width:330px;height:330px;border-radius:50%;border:14px solid #444a50;display:flex;align-items:center;justify-content:center;color:var(--blue);font-size:44px;font-weight:600}
.about-title{top:1655px;left:495px;font-size:26px;color:var(--blue);letter-spacing:1px}
.about-text{top:1718px;left:495px;width:620px;font-size:13.5px;line-height:18px;color:#555}

/* offerings */
.offer-photo{top:2087px;left:0;width:1200px;height:456px;background:linear-gradient(90deg,#e9ecef 0%,#d8dde3 40%,#c7ccd2 70%,#e5e2dd 100%)}
.offer-title{top:2150px;font-size:26px;font-weight:600;color:#222;letter-spacing:1px}
.card{top:2353px;width:342px;height:540px}
.card-top{height:190px;background:var(--white);display:flex;align-items:center;justify-content:center;font-size:30px;font-weight:700;color:#444}
.card-body{height:335px;background:var(--card-grey);padding:30px 14px 0;text-align:center}
.card-cat{font-size:14px;color:#777;letter-spacing:1px;text-transform:uppercase}
.card-name{font-family:"Roboto Condensed",sans-serif;font-size:32px;font-weight:700;color:var(--blue);margin-top:22px}
.card-desc{font-size:13px;color:#444;line-height:17px;margin-top:4px;height:36px}
.card-offer{font-size:15px;margin-top:12px;color:#222}
.card-stats{display:flex;justify-content:space-between;font-size:12px;margin-top:28px;color:#333}
.bar{height:18px;background:var(--white);margin-top:6px}
.bar span{display:block;height:18px;background:var(--blue)}
.card-meta{display:flex;justify-content:space-between;font-size:11px;color:#666;margin-top:4px}
.card .btn{position:absolute;bottom:-6px;left:96px;width:150px;height:30px;line-height:30px;font-size:13px}
.side-arrow{font-size:34px;color:#222}

/* partners */
.partner{top:3055px;font-size:30px;color:#333;display:flex;align-items:center;gap:10px}
.partner i{display:inline-block;width:34px;height:34px;border-radius:50%;border:3px solid #e07b2a}

/* testimonials */
.testi-band{top:3267px;left:0;width:1200px;height:406px;background:var(--grey-band)}
.quote{top:3290px;width:330px;height:200px;background:var(--white);padding:18px 16px;font-size:12px;line-height:16px;color:#777}
.quote b{display:block;margin-top:22px;font-size:14px;color:#222}
.quote small{font-size:11px;color:#888}
.avatar{top:3540px;width:166px;height:166px;border-radius:50%;border:6px solid #555;background:linear-gradient(#cfd6de,#a9b4bf)}

/* letter */
.letter-title{top:3810px;font-size:28px;color:var(--blue);letter-spacing:1px}
.letter-text{top:3870px;left:270px;width:660px;text-align:center;font-size:13px;line-height:18px;color:#444}
.field{top:3979px;width:250px;height:40px;border:1px solid #777;font-size:12px;padding:11px 8px}
.message{top:4035px;left:73px;width:1052px;height:190px;border:1px solid #777;font-size:12px;padding:10px 8px}
.send{top:4241px;left:880px;width:245px;height:40px;line-height:40px}

/* footer */
.footer{top:4334px;left:0;width:1200px;height:370px;background:var(--footer)}
.foot-title{top:4370px;font-size:26px;color:var(--white);letter-spacing:1px}
.foot-text{top:4425px;left:330px;width:540px;text-align:center;font-size:13px;line-height:18px;color:#cfd2d6}
.foot-social{top:4537px;width:92px;height:92px;border-radius:50%;border:5px solid var(--white);background:#2e3breal;display:flex;align-items:center;justify-content:center;color:var(--white);font-size:15px;font-weight:600;background:#2f353d}
.copy{top:4656px;font-size:13px;color:#cfd2d6}
.copy span{color:#5fa3e0}
.map{top:4704px;left:0;width:1200px;height:282px;background:linear-gradient(135deg,#dfe2e6,#cfd3d8 50%,#e5e7ea)}
</style>
</head>
<body>

<div class="abs hero" role="img" aria-label="Photo of a person writing at a desk beside a computer keyboard"></div>
<header class="abs nav">
  <div class="abs social-top" style="left:66px">Feed</div>
  <div class="abs social-top" style="left:116px">Page</div>
  <div class="abs social-top" style="left:166px">Circle</div>
  <span class="abs nav-link active" style="left:266px">Landing page</span>
  <span class="abs nav-link" style="left:405px">About us</span>
  <span class="abs nav-link" style="left:505px">Investors</span>
  <span class="abs nav-link" style="left:602px">Entrepreneurs</span>
  <span class="abs nav-link" style="left:738px">Crowdfunding</span>
  <span class="abs nav-link" style="left:871px">Contact</span>
  <div class="abs search">Search…
    <svg style="position:absolute;right:12px;top:10px" width="18" height="18" viewBox="0 0 18 18"><circle cx="7" cy="7" r="5.5" fill="none" stroke="#fff" stroke-width="2"/><line x1="11" y1="11" x2="16" y2="16" stroke="#fff" stroke-width="2.4"/></svg>
  </div>
</header>
<div class="abs arrow" style="left:12px">«</div>
<div class="abs arrow" style="left:1148px">»</div>
<div class="abs dots"><span class="dot on"></span><span class="dot"></span><span class="dot"></span><span class="dot"></span></div>

<h1 class="abs center welcome">WELCOME</h1>
<div class="abs brand-mark"></div>
<div class="abs center brand-name">BRIGHTFOLD CAPITAL</div>
<div class="abs center tagline">INVEST IN STARTUPS</div>
<div class="abs center tagline-sub">Get access to highly curated early and late stage investment opportunities</div>
<div class="abs btn" style="top:1405px;left:500px;width:200px">SIGN UP FOR FREE</div>

<section class="abs about"></section>
<div class="abs about-ring">Brightfold</div>
<h2 class="abs about-title">ABOUT OUR COMPANY</h2>
<p class="abs about-text">Our mission is to back founders who build companies that lift whole communities. We partner with growth teams early, guide them through every round, and connect them with investors who care about lasting impact. Our mission is to back founders who build companies that lift whole communities. We partner with growth teams early and stay close after each round closes.</p>
<div class="abs btn" style="top:1840px;left:495px;width:152px;height:30px;line-height:30px;font-size:13px">Read More</div>

<div class="abs offer-photo" role="img" aria-label="Photo of business people working at laptops in a bright office"></div>
<h2 class="abs center offer-title">CURRENT OFFERINGS</h2>
<div class="abs side-arrow" style="top:2645px;left:18px">‹</div>
<div class="abs side-arrow" style="top:2645px;left:1165px">›</div>

<article class="abs card" style="left:73px">
  <div class="card-top">Harborlight</div>
  <div class="card-body">
    <div class="card-cat">Restaurant &amp; Beverage</div>
    <div class="card-name">LONE MESA GRILL</div>
    <div class="card-desc">Coffee + bar + lounge and artisan pizzeria in Texas</div>
    <div class="card-offer">Offered by Civic Ledger VC</div>
    <div class="card-stats"><b>$48,267</b><span>38 investors</span></div>
    <div class="bar"><span style="width:48%"></span></div>
    <div class="card-meta"><span>48%</span><span>37 days left</span></div>
  </div>
  <div class="btn">Read More</div>
</article>
<article class="abs card" style="left:425px">
  <div class="card-top">Tuneyard</div>
  <div class="card-body">
    <div class="card-cat">Social Media</div>
    <div class="card-name">TUNEYARD</div>
    <div class="card-desc">Social marketplace for music collaboration and distribution</div>
    <div class="card-offer">Offered by Civic Ledger VC</div>
    <div class="card-stats"><b>$127,280</b><span>269 investors</span></div>
    <div class="bar"><span style="width:100%"></span></div>
    <div class="card-meta"><span>100%</span><span>26 days left</span></div>
  </div>
  <div class="btn">Read More</div>
</article>
<article class="abs card" style="left:778px">
  <div class="card-top"><span style="width:80px;height:80px;border-radius:50%;background:#24384a;display:block"></span></div>
  <div class="card-body">
    <div class="card-cat">Distillery</div>
    <div class="card-name">CAPITOL STILLHOUSE</div>
    <div class="card-desc">Urban distillery and craft cocktail bar located in Washington, D.C.</div>
    <div class="card-offer">Offered by Civic Ledger VC</div>
    <div class="card-stats"><b>$185,124</b><span>412 investors</span></div>
    <div class="bar"><span style="width:100%"></span></div>
    <div class="card-meta"><span>100%</span><span>15 days left</span></div>
  </div>
  <div class="btn">Read More</div>
</article>

<div class="abs side-arrow" style="top:3050px;left:18px">‹</div>
<div class="abs partner" style="left:75px">Cellforge</div>
<div class="abs partner" style="left:365px"><i></i>Genewell</div>
<div class="abs partner" style="left:700px;font-size:26px">Orbit Finch</div>
<div class="abs partner" style="left:945px">Foldwater</div>
<div class="abs side-arrow" style="top:3050px;left:1165px">›</div>
<div class="abs dots" style="top:3160px"><span class="dot on"></span><span class="dot"></span><span class="dot"></span><span class="dot"></span></div>

<section class="abs testi-band"></section>
<blockquote class="abs quote" style="left:73px">"Working with this team made our raise simple. They knew the right investors, kept us on schedule, and explained each step clearly so we could stay focused on building."<b>DANIEL MARSH</b><small>Founder &amp; Chief Executive</small></blockquote>
<blockquote class="abs quote" style="left:435px">"Working with this team made our raise simple. They knew the right investors, kept us on schedule, and explained each step clearly so we could stay focused on building."<b>CLARA ELLISON</b><small>Founder &amp; Chief Executive</small></blockquote>
<blockquote class="abs quote" style="left:795px">"Working with this team made our raise simple. They knew the right investors, kept us on schedule, and explained each step clearly so we could stay focused on building."<b>PETER HALE</b><small>Founder &amp; Chief Executive</small></blockquote>
<div class="abs avatar" style="left:155px" role="img" aria-label="Portrait photo of a client"></div>
<div class="abs avatar" style="left:517px" role="img" aria-label="Portrait photo of a client"></div>
<div class="abs avatar" style="left:877px" role="img" aria-label="Portrait photo of a client"></div>

<h2 class="abs center letter-title">WRITE US A LETTER</h2>
<p class="abs letter-text">Tell us about your company, your raise or your questions. Our team reads every note and replies within two business days with clear next steps.</p>
<div class="abs field" style="left:73px">First Name</div>
<div class="abs field" style="left:340px">Last Name</div>
<div class="abs field" style="left:607px">Contact no</div>
<div class="abs field" style="left:875px">E-mail Address</div>
<div class="abs message">Message</div>
<div class="abs btn send">SEND</div>

<footer class="abs footer"></footer>
<h2 class="abs center foot-title">CONTACT US</h2>
<p class="abs foot-text">Reach our offices during business hours or send a note any time. We welcome founders, investors and finance partners who share our focus on impact.</p>
<div class="abs foot-social" style="left:427px">Feed</div>
<div class="abs foot-social" style="left:554px">Page</div>
<div class="abs foot-social" style="left:681px">Circle</div>
<div class="abs center copy"><span>Brightfold Capital</span> © 2016 Privacy Policy. Terms of use</div>
<div class="abs map" role="img" aria-label="Street map showing the office location"></div>
<svg class="abs" style="top:4805px;left:586px" width="28" height="40" viewBox="0 0 28 40"><path d="M14 0C6 0 0 6 0 14c0 10 14 26 14 26s14-16 14-26C28 6 22 0 14 0z" fill="#111"/><circle cx="14" cy="14" r="5" fill="#fff"/></svg>

</body>
</html>
```